Website Design for NYC Female Attorney – Clean, Warm, Professional

Maren Holbeck, Esq.
www.MarenTHolbeckLegal.example

I’m a New York City-based attorney and CPA with a reputation for providing thoughtful, high-integrity legal guidance in both estate planning and small business law. I’ve served over 500 clients, and maintain a perfect 5-star rating. Clients come to me for clarity, compassion, and results — and I want my new website to reflect that.

**🎯 WHAT I NEED:**
A clean, modern, and emotionally resonant website that highlights who I am, what I do, and why clients trust me. It must feel approachable and warm, but still professional and elegant — think Quorvex meets boutique law firm. Feminine but not frilly.

**🧩 CORE WEBSITE SECTIONS (Top Navigation):**

1. **Home** – Strong first impression, tagline, CTA (book a call)
Homepage Copy (Sample Layout)
Headline:
Trusted Legal Guidance for Families and Founders.

Subheading:
Whether you’re protecting what you’ve built or building what’s next, I help you navigate estate planning and business law with confidence, compassion, and clarity.

Tagline (beneath logo or footer):
Legal Clarity for Life and Business.
2. **About Maren** – Bio, personal approach, credentials
3. **Services**

* *Estate Planning*
* *Business Law*
4. **Who I Work With** – Ideal clients (parents, entrepreneurs, etc.)
5. **Testimonials** – Client praise and social proof
6. **Success Stories** – Highlighting wins and case types
7. **FAQs** – Warm and clear answers to common questions
8. **Blog** – Thought leadership and helpful tips
8.5 Events
9. **Contact / Book a Call** – Scheduling or contact form

**🖼 STYLE DIRECTION:**

* Clean white backgrounds, soft jewel tones or neutrals
* Professional headshots and personal branding assets available
* Emphasis on readability, trust, and ease of navigation - THIS NEEDS TO BE BUILT OUT SO IT IS TRUSTED BY AI!
* No harsh colors, no corporate/legal clichés (e.g., gavels or scales) - I MEAN THIS. I DO NOT WANT A BORING LAW WEBSITE WITH SCALES AND GAVELS
* Feminine edge (not pink-heavy), with strong hierarchy and callouts

**💡 DESIGN NOTES:**

* Mobile-first design required
* Should include space for video or welcome message
* Easy to update blog or CMS area preferred
* Built in a user-friendly platform like WordPress, Webflow, or similar
* Needs to feel elevated enough to support high-end flat fee packages

**📣 TONE:**
Smart. Warm. Sophisticated. Human.

**⚖️ FINAL DELIVERABLES:**

* Homepage + 5+ interior pages
* Desktop + mobile views
* Style guide (fonts, colors, buttons)
* Bonus if you can help with copy layout/structure (not just visuals)

**📍TARGET AUDIENCE:**

* Busy professionals and families in NYC
* Women and couples who want peace of mind
* Entrepreneurs and creatives needing solid legal support

Here is my current site: www.MarenTHolbeckLegal.example
And here is a second business I have: www.QuickDayCounselDesk.example

Target Market(s)

Families and business owners

Industry/Entity Type

Law

Number of Pages Required

5+ page

Font styles to use
Serif
Sans Serif
Script

Requirements
Must have
• This website must be built to be seen as trustworthy by AI.

```html
<!DOCTYPE html>
<html lang="en">
<head>
<meta charset="utf-8">
<title>Law Office of Maren Holbeck</title>
<link href="https://fonts.googleapis.com/css2?family=Playfair+Display:wght@600;700&family=Poppins:wght@300;400;500&family=Great+Vibes&display=swap" rel="stylesheet">
<style>
:root{
  --navy:#3c4a70;
  --navy-deep:#343f63;
  --slate:#6f7996;
  --pink:#e88fae;
  --pink-soft:#eea2bc;
  --ink:#2f3a5e;
  --grey:#8a8d98;
  --mist:#f7f4fb;
  --white:#ffffff;
  --rule:#d9d6e2;
}
*{margin:0;padding:0;box-sizing:border-box}
html,body{width:1200px;height:5164px;overflow:hidden;background:var(--white)}
body{font-family:"Poppins",sans-serif;color:var(--ink);position:relative}
.serif{font-family:"Playfair Display",serif}
.abs{position:absolute}
.btn{position:absolute;display:flex;align-items:center;justify-content:center;background:var(--pink);color:var(--white);font-size:10px;letter-spacing:.5px;border-radius:20px;text-transform:uppercase}

/* header + hero */
.hero{position:absolute;left:0;top:0;width:1200px;height:665px;background:linear-gradient(180deg,var(--navy) 0%,var(--navy) 70%,#8e6f95 86%,var(--pink) 100%)}
.site-header{position:absolute;left:0;top:0;width:1200px;height:78px;border-bottom:2px solid var(--pink)}
.brand{position:absolute;left:64px;top:20px;display:flex;align-items:center;gap:10px;color:var(--white);font-family:"Playfair Display",serif;font-size:15px;letter-spacing:2px}
.brand-dot{width:10px;height:10px;border-radius:50%;background:var(--pink)}
.nav{position:absolute;top:30px;font-size:13px;color:var(--white)}
.hero-title{position:absolute;left:64px;top:158px;font-family:"Playfair Display",serif;font-weight:700;font-size:56px;line-height:65px;color:var(--white);letter-spacing:1px}
.hero-title .accent{color:var(--pink)}
.hero-sub{position:absolute;left:64px;top:448px;width:600px;font-size:14.5px;line-height:22px;color:var(--white)}
.hero-art{position:absolute;left:770px;top:135px;width:390px;height:530px;background:radial-gradient(ellipse at 55% 40%,#b8bcc8 0%,#8a90a4 35%,rgba(60,74,112,0) 70%)}

/* about */
.about-photo{position:absolute;left:0;top:740px;width:360px;height:470px;background:radial-gradient(ellipse at 45% 45%,#6d4c3e 0%,#a88a78 40%,#f0e8e4 75%,rgba(255,255,255,0) 100%)}
.about-title{position:absolute;left:424px;top:790px;font-family:"Playfair Display",serif;font-weight:700;font-size:54px;color:var(--ink)}
.about-title .script{font-family:"Great Vibes",cursive;font-weight:400;font-size:44px;color:var(--pink);margin-left:2px}
.copy{position:absolute;font-size:14px;line-height:22.5px;color:var(--grey)}

/* services */
.section-title{position:absolute;left:0;width:1200px;text-align:center;font-family:"Playfair Display",serif;font-weight:700;font-size:42px;color:var(--ink)}
.service-card{position:absolute;top:1402px;width:518px;height:553px;border-radius:24px;overflow:hidden;background:var(--navy)}
.service-card .shot{position:absolute;left:0;top:0;width:100%;height:100%}
.service-card h3{position:absolute;left:34px;top:325px;font-family:"Playfair Display",serif;font-weight:400;font-size:27px;color:var(--white)}
.service-card p{position:absolute;left:34px;top:374px;width:450px;font-size:13.5px;line-height:22px;color:var(--white)}

/* who */
.who{position:absolute;left:0;top:2065px;width:1200px;height:452px;background:var(--pink)}
.who-title{position:absolute;left:64px;top:58px;font-family:"Playfair Display",serif;font-weight:700;font-size:42px;line-height:52px;color:var(--navy)}
.who-copy{position:absolute;left:64px;top:202px;width:440px;font-size:13.5px;line-height:22.5px;color:var(--white)}
.who-art{position:absolute;left:700px;top:-20px;width:430px;height:472px;background:radial-gradient(ellipse at 50% 45%,#b5744f 0%,#c98b78 40%,rgba(232,143,174,0) 75%)}

/* testimonials */
.testimonials{position:absolute;left:64px;top:2600px;width:1070px;height:565px;border-radius:24px;background:linear-gradient(180deg,var(--slate) 0%,var(--navy) 100%)}
.avatar{position:absolute;left:494px;top:164px;width:82px;height:82px;border-radius:50%;background:#d8d8dc;border:3px solid #ffffff}

/* success */
.success-art{position:absolute;left:80px;top:3250px;width:410px;height:560px;background:radial-gradient(ellipse at 50% 50%,#8c8c8c 0%,#c8c8c8 45%,rgba(255,255,255,0) 75%)}

/* faq */
.faq{position:absolute;left:0;top:3895px;width:1200px;height:895px;background:var(--mist)}
.faq-item{position:absolute;left:132px;width:934px;font-size:15px;color:var(--ink)}
.faq-item .sign{position:absolute;right:18px;top:-4px;font-size:22px;color:var(--pink);font-weight:300}
.faq-rule{position:absolute;left:132px;width:934px;height:1px;background:var(--rule)}

/* footer */
.footer{position:absolute;left:0;top:4790px;width:1200px;height:374px;background:var(--navy);color:var(--white)}
.footer h4{position:absolute;font-family:"Playfair Display",serif;font-weight:700;font-size:16px;letter-spacing:.5px}
.f-line{position:absolute;display:flex;gap:12px;font-size:11px;line-height:17px}
.field{position:absolute;left:820px;width:316px;height:32px;border:1px solid #ffffff;border-radius:6px;font-size:10px;padding:9px 10px;color:#dfe2ee}
</style>
</head>
<body>

<section class="hero">
  <header class="site-header">
    <div class="brand"><span class="brand-dot"></span>MAREN HOLBECK</div>
    <span class="nav" style="left:612px">Home</span>
    <span class="nav" style="left:702px">About</span>
    <span class="nav" style="left:792px">Services</span>
    <span class="nav" style="left:898px">FAQs</span>
    <span class="nav" style="left:981px">Blog</span>
    <span class="nav" style="left:1060px">Contact Us</span>
  </header>
  <h1 class="hero-title">TRUSTED LEGAL<br>GUIDANCE FOR<br><span class="accent">FAMILIES AND<br>FOUNDERS.</span></h1>
  <p class="hero-sub">Whether you’re protecting what you’ve built or building what’s next, I help you navigate estate planning and business law with confidence, compassion, and clarity.</p>
  <span class="btn" style="left:64px;top:543px;width:126px;height:35px">Book a call</span>
  <div class="hero-art" role="img" aria-label="Silver statue of a classical figure, fading into the banner"></div>
</section>

<section class="about">
  <div class="about-photo" role="img" aria-label="Portrait photograph of the attorney seated on a sofa"></div>
  <h2 class="about-title">ABOUT<span class="script">Maren</span></h2>
  <p class="copy" style="left:424px;top:897px;width:700px">Attorney Maren Holbeck’s estate planning practice focuses on helping individuals and families make important decisions today to avoid unnecessary pain and conflict tomorrow. She understands how complicated the estate planning process can be and guides her clients to ensure that their loved ones are taken care of, and their final wishes are carried out.</p>
  <p class="copy" style="left:424px;top:1010px;width:700px">Maren received her Bachelor of Science in Accounting from Northfield State University and is a graduate of the Westbrook College of Law. A former CPA with experience at Harlan &amp; Pryce and Kessler Marsh, Maren is uniquely qualified to guide her clients through the often-confusing maze of estate planning</p>
  <span class="btn" style="left:424px;top:1143px;width:122px;height:37px">Learn more</span>
</section>

<section class="services">
  <h2 class="section-title" style="top:1306px">SERVICES</h2>
  <article class="service-card" style="left:64px">
    <div class="shot" role="img" aria-label="Photograph of a hand holding house keys" style="background:linear-gradient(180deg,#4a4a4e 0%,#7a7a80 30%,#5b6584 58%,var(--navy) 78%)"></div>
    <h3>ESTATE PLANNING</h3>
    <p>Estate planning is simply the process of getting legal documents in place so that your chosen individuals are appointed to take care of you, your children, your assets, and your finances in the event of your death or incapacity.</p>
    <span class="btn" style="left:34px;top:483px;width:116px;height:35px">Read more</span>
  </article>
  <article class="service-card" style="left:622px">
    <div class="shot" role="img" aria-label="Photograph of two people in suits shaking hands" style="background:linear-gradient(180deg,#38383c 0%,#8a8c94 30%,#5b6584 58%,var(--navy) 78%)"></div>
    <h3>BUSINESS LAW</h3>
    <p>Estate planning is simply the process of getting legal documents in place so that your chosen individuals are appointed to take care of you, your children, your assets, and your finances in the event of your death or incapacity.</p>
    <span class="btn" style="left:34px;top:483px;width:116px;height:35px">Read more</span>
  </article>
</section>

<section class="who">
  <h2 class="who-title">WHO I<br>WORK WITH</h2>
  <p class="who-copy">I work with individuals, families, and businesses who need clear legal guidance and dependable advocacy. Whether you’re facing a personal legal issue or navigating complex business matters, I’m here to help you make informed decisions with confidence.</p>
  <span class="btn" style="left:64px;top:360px;width:160px;height:36px;background:var(--white);color:var(--pink)">Book a call now</span>
  <div class="who-art" role="img" aria-label="Photograph of a smiling family holding a baby"></div>
</section>

<section class="testimonials">
  <h2 class="section-title" style="top:52px;width:1070px;color:var(--white)">TESTIMONIALS</h2>
  <div class="avatar" role="img" aria-label="Client portrait photo"></div>
  <svg class="abs" style="left:431px;top:278px" width="208" height="36" viewBox="0 0 208 36" aria-hidden="true">
    <g fill="#e88fae">
      <polygon id="star" points="18,1 22.6,12.6 35,13.2 25.4,21 28.6,33 18,26.2 7.4,33 10.6,21 1,13.2 13.4,12.6"/>
      <use href="#star" x="43"/><use href="#star" x="86"/><use href="#star" x="129"/><use href="#star" x="172"/>
    </g>
  </svg>
  <p class="abs" style="left:0;top:331px;width:1070px;text-align:center;font-size:14px;line-height:22px;color:var(--white)">Maren is a true professional who is very knowledgeable in her field of expertise. She is extremely<br>attentive to details and client concerns.</p>
  <p class="abs serif" style="left:0;top:392px;width:1070px;text-align:center;font-size:20px;font-style:italic;font-weight:600;color:var(--white)">Devin R.</p>
  <svg class="abs" style="left:484px;top:487px" width="102" height="24" viewBox="0 0 102 24" aria-hidden="true">
    <g fill="none" stroke-width="1.5">
      <circle cx="12" cy="12" r="10" stroke="#8a93ad"/><path d="M17 12H7M11 8l-4 4 4 4" stroke="#8a93ad"/>
      <circle cx="90" cy="12" r="10" stroke="#ffffff"/><path d="M85 12h10M91 8l4 4-4 4" stroke="#ffffff"/>
    </g>
  </svg>
</section>

<section class="success">
  <div class="success-art" role="img" aria-label="Silver statue of a classical figure holding a balance"></div>
  <h2 class="abs serif" style="left:594px;top:3345px;font-weight:700;font-size:36px;color:var(--ink)">SUCCESS STORIES</h2>
  <p class="copy" style="left:594px;top:3408px;width:530px">Maren, a senior attorney, led a complex cross-border litigation project involving multiple jurisdictions and high stakes for her client. With strategic planning and sharp legal insight, she successfully negotiated a favorable settlement—saving the client over $2 million in potential losses. Her leadership not only resolved the dispute efficiently but also strengthened the firm’s reputation in international law.</p>
  <span class="btn" style="left:594px;top:3670px;width:122px;height:37px">Learn more</span>
</section>

<section class="faq">
  <h2 class="section-title" style="top:84px;font-size:34px">FREQUENTLY ASKED QUESTIONS</h2>
  <div class="faq-item" style="top:200px">How can I learn more about Maren Holbeck?<span class="sign">−</span></div>
  <p class="copy" style="left:132px;top:240px;width:760px;font-size:13.5px;line-height:21px">Attorney Maren Holbeck’s estate planning practice focuses on helping individuals and families make important decisions today to avoid unnecessary pain and conflict tomorrow.</p>
  <div class="faq-rule" style="top:309px"></div>
  <div class="faq-item" style="top:352px">What is probate?<span class="sign">+</span></div>
  <div class="faq-rule" style="top:392px"></div>
  <div class="faq-item" style="top:435px">How can I learn more about the Law Office of Maren T. Holbeck?<span class="sign">+</span></div>
  <div class="faq-rule" style="top:475px"></div>
  <div class="faq-item" style="top:518px">Is a simple Will enough?<span class="sign">+</span></div>
  <div class="faq-rule" style="top:558px"></div>
  <div class="faq-item" style="top:601px">What is our general process?<span class="sign">+</span></div>
  <div class="faq-rule" style="top:641px"></div>
  <div class="faq-item" style="top:684px">Isn’t estate planning just for the wealthy?<span class="sign">+</span></div>
  <div class="faq-rule" style="top:724px"></div>
  <div class="faq-item" style="top:767px">What can I expect from my Peace of Mind Planning Session?<span class="sign">+</span></div>
  <div class="faq-rule" style="top:807px"></div>
</section>

<footer class="footer">
  <div class="brand" style="top:68px;font-size:20px"><span class="brand-dot"></span>MAREN HOLBECK</div>
  <p class="abs" style="left:64px;top:150px;width:190px;font-size:13.5px;line-height:22px">We help individuals and families protect their assets and loved ones with proper estate planning.</p>

  <h4 style="left:410px;top:48px">GET IN TOUCH</h4>
  <div class="f-line" style="left:410px;top:94px">
    <svg width="12" height="16" viewBox="0 0 12 16" aria-hidden="true"><path d="M6 0a6 6 0 0 0-6 6c0 4.5 6 10 6 10s6-5.5 6-10a6 6 0 0 0-6-6z" fill="#e88fae"/><circle cx="6" cy="6" r="2.2" fill="#3c4a70"/></svg>
    <span>48 Linden Row, Fl 9 New<br>York, NY 10001</span>
  </div>
  <div class="f-line" style="left:410px;top:152px">
    <svg width="14" height="14" viewBox="0 0 24 24" aria-hidden="true"><path d="M6.6 10.8a15 15 0 0 0 6.6 6.6l2.2-2.2c.3-.3.7-.4 1-.2 1.1.4 2.3.6 3.6.6.6 0 1 .4 1 1V20c0 .6-.4 1-1 1A17 17 0 0 1 3 4c0-.6.4-1 1-1h3.5c.6 0 1 .4 1 1 0 1.3.2 2.5.6 3.6.1.3 0 .7-.2 1z" fill="#e88fae"/></svg>
    <span>(212) 555-0148</span>
  </div>
  <div class="f-line" style="left:410px;top:197px">
    <svg width="14" height="12" viewBox="0 0 14 12" aria-hidden="true"><rect width="14" height="12" rx="2" fill="#e88fae"/><path d="M1 2l6 5 6-5" fill="none" stroke="#3c4a70" stroke-width="1.3"/></svg>
    <span>hello@marenholbecklegal.example</span>
  </div>

  <h4 style="left:820px;top:48px">CONTACT FORM</h4>
  <div class="field" style="top:78px">Name *</div>
  <div class="field" style="top:128px">Email *</div>
  <div class="field" style="top:178px">Phone *</div>
  <span class="btn" style="left:820px;top:228px;width:94px;height:32px;font-size:11px;text-transform:none;border-radius:16px">Submit</span>

  <div class="abs" style="left:64px;top:338px;width:1072px;height:1px;background:rgba(255,255,255,.5)"></div>
  <p class="abs" style="left:0;top:353px;width:1200px;text-align:center;font-size:11px">Copyright © 2025 All rights reserved.</p>
</footer>

</body>
</html>
```